I want both print and ebook covers

book title is "The Classroom MEETING HANDBOOK: Fresh Paths to Partner With Families For Pupil Growth. I want a dark Teal or Navy Background. Yellow and white letters. Distorted Picture of one teacher, two parents and one child around a table or desk. But no Martians! My name should include "Award Winning Author"

Target Market(s)

teachers and other educators--principals, school psychologists, speech therapists, etc.

Industry/Entity Type

schools

• I just need to see how it looks

Colors
0054AA
0677BA
7BADD7
CADEEF
E8F1F8
0094D4
00A9DD
6FCCEA
C7EBF8
E9F6FB
FFC000
F8CF3A
FAE287
FDF2CF
FEFAEE

Requirements
Must have
• Title top third of page big enough to be read when reduced greatly in size. Contrast so that it "pops'.
Nice to have
• Teacher, two parents and one child around a table/desk. My name should include 'Award winning author'

```html
<!DOCTYPE html>
<html lang="en">
<head>
<meta charset="utf-8">
<title>The Classroom Meeting Handbook – Cover</title>
<link rel="stylesheet" href="https://fonts.googleapis.com/css2?family=Arimo:wght@700&display=swap">
<style>
  :root {
    --page-bg: #e9e9e9;
    --cover-navy: #0c2d57;
    --floor-blue: #0054aa;
    --title-white: #ffffff;
    --title-yellow: #ffc000;
    --subtitle-blue: #c7ebf8;
    --art-sky: #6fccea;
    --art-blue: #0677ba;
    --art-sun: #f8cf3a;
  }
  * { margin: 0; padding: 0; box-sizing: border-box; }
  html, body {
    width: 1200px;
    height: 1200px;
    overflow: hidden;
    background: var(--page-bg);
  }
  .book-cover {
    position: absolute;
    left: 241px;
    top: 63px;
    width: 718px;
    height: 1074px;
    background: var(--cover-navy);
    overflow: hidden;
  }
  .floor-band {
    position: absolute;
    left: 0;
    right: 0;
    top: 796px;
    bottom: 0;
    background: var(--floor-blue);
  }
  .cover-title {
    position: absolute;
    left: 0;
    top: 0;
    width: 718px;
    height: 540px;
  }
  .cover-title text { font-family: "Arimo", Arial, sans-serif; font-weight: 700; }
  .title-white { fill: var(--title-white); }
  .title-yellow { fill: var(--title-yellow); }
  .title-sub { fill: var(--subtitle-blue); }
  .conference-scene {
    position: absolute;
    left: 42px;
    top: 556px;
    width: 625px;
    height: 440px;
    border-radius: 6px;
    background: linear-gradient(135deg, var(--art-sun) 0%, var(--art-sky) 50%, var(--art-blue) 100%);
    opacity: 0.45;
  }
  .author-line {
    position: absolute;
    left: 0;
    top: 0;
    width: 718px;
    height: 1074px;
    pointer-events: none;
  }
  .author-line text {
    font-family: "Arimo", Arial, sans-serif;
    font-weight: 700;
    fill: var(--title-yellow);
  }
</style>
</head>
<body>
  <main class="book-cover">
    <div class="floor-band"></div>

    <svg class="cover-title" viewBox="0 0 718 540" aria-label="The Classroom Meeting Handbook: Fresh Paths to Partner With Families For Pupil Growth">
      <text class="title-white" x="359" y="95" font-size="64" text-anchor="middle" textLength="124" lengthAdjust="spacingAndGlyphs">THE</text>
      <text class="title-white" x="359" y="192" font-size="117" text-anchor="middle" textLength="632" lengthAdjust="spacingAndGlyphs">CLASSROOM</text>
      <text class="title-yellow" x="359" y="317" font-size="154" text-anchor="middle" textLength="632" lengthAdjust="spacingAndGlyphs">MEETING</text>
      <text class="title-white" x="359" y="452" font-size="160" text-anchor="middle" textLength="632" lengthAdjust="spacingAndGlyphs">HANDBOOK</text>
      <text class="title-sub" x="359" y="497" font-size="27" text-anchor="middle">Fresh Paths to Partner With Families</text>
      <text class="title-sub" x="359" y="531" font-size="27" text-anchor="middle">For Pupil Growth</text>
    </svg>

    <div class="conference-scene" role="img" aria-label="Illustration of a teacher at a desk with a laptop and plant, talking with two parents and a child seated in chairs, with small confetti stars above"></div>

    <svg class="author-line" viewBox="0 0 718 1074" aria-label="Award Winning Author">
      <text x="359" y="1052" font-size="42" text-anchor="middle" textLength="512" lengthAdjust="spacingAndGlyphs">AWARD WINNING AUTHOR</text>
    </svg>
  </main>
</body>
</html>
```